Velisto Events Business Card

We need a business cards that stands out to our clients. We are company who targets prestige clients to spend money with us on experiences, so our image needs to be prestige
Target Market(s)
Corporate
Contact Information for Business Card
There will be four different names on the business cards
Dana Morrowby
Director
O: 02 5147 3086
M: 0451 692 038
E: info@velistoevents.example.au
Facebook: @velistoevents
Instagram: velistoevents
www.velistoevents.example.au
Nathaniel Morrowby
Director
O: 02 5147 3086
M: 0467 215 904
Facebook: @velistoevents
Instagram: velistoevents
www.velistoevents.example.au
Teodor Vinkel
Director
O: 02 5147 3086
M: 0478 903 527
Facebook: @velistoevents
Instagram: velistoevents
www.velistoevents.example.au
Mabel Hartung
Director
O: 02 5147 3086
Facebook: @velistoevents
Instagram: velistoevents
www.velistoevents.example.au
Colors
Designer to choose colors to be used in the design.
Look and feel

```html
<!DOCTYPE html>
<html lang="en">
<head>
<meta charset="utf-8">
<title>Velisto Events Business Card</title>
<link rel="stylesheet" href="https://fonts.googleapis.com/css2?family=Montserrat:wght@400;500;600&display=swap">
<style>
  :root {
    --page-bg: #e9e6e1;
    --card-navy-deep: #25246a;
    --card-navy-light: #4a4888;
    --gold: #e2b548;
    --ink-white: #f2f1f8;
  }
  * { box-sizing: border-box; margin: 0; padding: 0; }
  html, body {
    width: 1200px;
    height: 900px;
    overflow: hidden;
    background: var(--page-bg);
    font-family: "Montserrat", sans-serif;
  }
  .canvas {
    position: relative;
    width: 1200px;
    height: 900px;
  }
  .card {
    position: absolute;
    top: 285px;
    width: 540px;
    height: 330px;
    overflow: hidden;
    background: radial-gradient(ellipse at 40% 35%, var(--card-navy-light) 0%, var(--card-navy-deep) 85%);
    box-shadow: 0 10px 28px rgba(30, 25, 60, 0.28);
    color: var(--ink-white);
  }
  .card--front { left: 40px; }
  .card--back { left: 620px; }

  .wordmark {
    color: var(--gold);
    font-weight: 500;
    text-transform: uppercase;
    letter-spacing: 0.28em;
    text-align: center;
    line-height: 1.5;
  }
  .card--front .wordmark {
    position: absolute;
    left: 0; right: 0;
    top: 130px;
    font-size: 24px;
  }
  .website {
    position: absolute;
    left: 0; right: 0;
    top: 232px;
    text-align: center;
    font-size: 13px;
    letter-spacing: 0.06em;
  }
  .website .accent { color: var(--gold); }

  .card--back .wordmark {
    position: absolute;
    left: 20px;
    width: 200px;
    top: 138px;
    font-size: 19px;
  }
  .divider {
    position: absolute;
    left: 234px;
    top: 72px;
    width: 1.5px;
    height: 186px;
    background: var(--ink-white);
  }
  .contact {
    position: absolute;
    left: 254px;
    right: 18px;
    top: 90px;
  }
  .contact__name {
    color: var(--gold);
    font-weight: 600;
    font-size: 20px;
    letter-spacing: 0.02em;
    white-space: nowrap;
  }
  .contact__role {
    font-size: 14px;
    margin-top: 2px;
    margin-bottom: 18px;
  }
  .contact__list { list-style: none; }
  .contact__item {
    display: flex;
    align-items: center;
    gap: 10px;
    font-size: 13px;
    letter-spacing: 0.01em;
    margin-bottom: 7px;
    white-space: nowrap;
  }
  .contact__icon {
    width: 12px;
    height: 12px;
    flex: none;
  }
  .contact__dot {
    width: 10px;
    height: 10px;
    flex: none;
    margin: 0 1px;
    background: var(--gold);
  }
  .contact__dot--round { border-radius: 50%; }
</style>
</head>
<body>
<main class="canvas">
  <section class="card card--front" aria-label="Card front">
    <p class="wordmark">Velisto Events</p>
    <p class="website">www.<span class="accent">velistoevents</span>.example.au</p>
  </section>

  <section class="card card--back" aria-label="Card back">
    <p class="wordmark">Velisto Events</p>
    <div class="divider"></div>
    <div class="contact">
      <p class="contact__name">Dana Morrowby</p>
      <p class="contact__role">Director</p>
      <ul class="contact__list">
        <li class="contact__item">
          <svg class="contact__icon" viewBox="0 0 12 12" aria-hidden="true">
            <rect x="3" y="0.5" width="6" height="11" rx="1" fill="none" stroke="var(--gold)" stroke-width="1.2"/>
            <line x1="5" y1="9.5" x2="7" y2="9.5" stroke="var(--gold)" stroke-width="1"/>
          </svg>
          0451 692 038
        </li>
        <li class="contact__item">
          <span class="contact__dot" aria-hidden="true"></span>
          velistoevents
        </li>
        <li class="contact__item">
          <span class="contact__dot contact__dot--round" aria-hidden="true"></span>
          @velistoevents
        </li>
        <li class="contact__item">
          <svg class="contact__icon" viewBox="0 0 12 12" aria-hidden="true">
            <rect x="0.5" y="2.5" width="11" height="7.5" fill="var(--gold)"/>
            <polyline points="0.8,2.8 6,7 11.2,2.8" fill="none" stroke="var(--card-navy-deep)" stroke-width="1"/>
          </svg>
          info@velistoevents.example.au
        </li>
      </ul>
    </div>
  </section>
</main>
</body>
</html>
```